Poster design for "A Frame" Sign

I need a design for an A Frame sign. Measurements and Specifications here:
http://www.brodexsupply.com.au/pg/a-boards/ABPBBLKPRT-Print-Specs.pdf

Actually, it will need to be two designs, one with an arrow pointing left and one with an arrow pointing right, otherwise exactly the same.

LOGO to be used is attached. Colours of design should match logo and should also include orange tones.

The A Frame sign is to be put on the driveway of my home studio at a main road in a residential suburban area. Cars drive by at around 50 km/h, so there needs to be an eye catcher that there is a nurturing home massage studio here.

Logo can be left or right, somehow incorporated into the text below:
-
[Big header, ideally "LeHavre" font]
Tarova Calm
Massage Studio

[slightly smaller font, serif, with bullet points]
- Relaxation Massage
- Remedial Massage
- Pregnancy Massage
- Kahuna Massage

[big Arrow to the left/right - one for each side of the frame]

[sans serif font, same size as above]
Bookings essential!
ph 0491 857 604
www.tarovacalm.com.au

[serif font, same as above]
EFTPOS and instant health fund claims available.
-

Residential

f37022

```html
<!DOCTYPE html>
<html lang="en">
<head>
<meta charset="utf-8">
<title>Tarova Calm – Massage Studio A-Frame Sign</title>
<link rel="stylesheet" href="https://fonts.googleapis.com/css2?family=Josefin+Sans:wght@600;700&family=Fredoka:wght@600&family=Tinos&display=swap">
<style>
  :root {
    --surround: #5f6062;
    --pink: #e0287a;
    --pink-deep: #c81d66;
    --maroon: #8a1c3c;
    --orange: #f37022;
    --orange-soft: #f9a66a;
    --cream: #fff8f2;
    --white: #ffffff;
    --shadow: rgba(60, 20, 20, 0.35);
  }
  * { box-sizing: border-box; margin: 0; padding: 0; }
  html, body { width: 868px; height: 1200px; overflow: hidden; }
  body { background: var(--surround); position: relative; }

  .sign {
    position: absolute; left: 71px; top: 20px; width: 750px; height: 1129px;
    background: linear-gradient(180deg, var(--white) 0%, var(--cream) 22%, #fde2cc 45%, var(--orange-soft) 72%, var(--orange) 100%);
    overflow: hidden;
  }

  .title-bar {
    position: absolute; left: 0; top: 5px; width: 100%; height: 123px;
    background: var(--pink);
    box-shadow: 0 6px 8px var(--shadow);
    display: flex; align-items: center; justify-content: center;
  }
  .title-bar__name {
    font-family: "Josefin Sans", sans-serif; font-weight: 600;
    font-variant: small-caps; font-size: 82px; letter-spacing: 3px;
    color: var(--white); line-height: 1;
    text-shadow: 2px 3px 3px var(--shadow);
  }
  .subtitle {
    position: absolute; left: 0; top: 134px; width: 100%; text-align: center;
    font-family: "Fredoka", sans-serif; font-weight: 600; font-size: 56px;
    letter-spacing: 1px; color: var(--orange); line-height: 1;
    -webkit-text-stroke: 1.5px #b8430c;
    text-shadow: 3px 3px 2px rgba(80, 40, 20, 0.45);
  }

  .brand-mark {
    position: absolute; left: 30px; top: 257px; width: 354px; height: 354px;
    border-radius: 50%; background: var(--maroon);
    display: flex; align-items: center; justify-content: center;
  }
  .brand-mark__name {
    font-family: "Tinos", serif; font-size: 44px; color: var(--white);
  }

  .services {
    position: absolute; left: 400px; top: 257px; width: 320px;
  }
  .services__heading {
    font-family: "Tinos", serif; font-size: 34px; line-height: 40px;
    color: var(--orange); text-align: center; margin-bottom: 26px;
  }
  .services__list { list-style: none; }
  .services__item {
    height: 50px; margin-bottom: 20px;
    background: var(--pink); border: 4px solid var(--white);
    box-shadow: 2px 3px 5px var(--shadow);
    font-family: "Tinos", serif; font-size: 28px; color: var(--white);
    display: flex; align-items: center; justify-content: center;
  }

  .payment-note {
    position: absolute; left: 52px; top: 650px;
    font-family: "Tinos", serif; font-size: 25px; color: var(--pink);
  }

  .phone-bubble { position: absolute; left: 180px; top: 712px; width: 440px; height: 140px; }
  .phone-bubble__number {
    position: absolute; left: 102px; top: 22px;
    font-family: "Tinos", serif; font-size: 46px; color: var(--white); line-height: 1;
  }

  .bookings {
    position: absolute; left: 52px; top: 846px;
    font-family: "Josefin Sans", sans-serif; font-weight: 700;
    font-variant: small-caps; font-size: 64px; letter-spacing: 2px;
    color: var(--maroon); line-height: 1;
    text-shadow: 2px 2px 2px rgba(255, 255, 255, 0.25);
  }
  .website {
    position: absolute; left: 0; top: 940px; width: 100%; text-align: center;
    font-family: "Tinos", serif; font-size: 36px; color: var(--white);
    text-shadow: 2px 2px 3px var(--shadow);
  }

  .direction-ribbon { position: absolute; left: 0; top: 1016px; width: 660px; height: 80px; }
  .direction-ribbon__name {
    position: absolute; left: 150px; top: 20px;
    font-family: "Tinos", serif; font-size: 32px; color: var(--white); line-height: 1;
  }
</style>
</head>
<body>
  <main class="sign">
    <header class="title-bar">
      <h1 class="title-bar__name">Tarova Calm</h1>
    </header>
    <h2 class="subtitle">MASSAGE STUDIO</h2>

    <div class="brand-mark">
      <span class="brand-mark__name">Tarova Calm</span>
    </div>

    <section class="services">
      <h3 class="services__heading">MASSAGE<br>POSSIBLE:</h3>
      <ul class="services__list">
        <li class="services__item">Relaxation Massage</li>
        <li class="services__item">Remedial Massage</li>
        <li class="services__item">Pregnancy Massage</li>
        <li class="services__item">Kahuna Massage</li>
      </ul>
    </section>

    <p class="payment-note">EFTPOS and instant health fund claims available!</p>

    <div class="phone-bubble">
      <svg width="440" height="140" viewBox="0 0 440 140" aria-hidden="true">
        <path d="M18 4 H410 Q428 4 428 22 V96 Q428 114 410 114 H70 L30 138 L40 114 H18 Q4 114 4 96 V22 Q4 4 18 4 Z" fill="#ffffff" style="filter:drop-shadow(2px 3px 3px rgba(60,20,20,.35))"/>
        <rect x="22" y="18" width="390" height="82" rx="10" fill="#e0287a"/>
        <path d="M66 32 q-14 6 -12 28 q4 22 22 30 l8 -10 q2 -3 -1 -5 l-9 -6 q-3 -2 -5 1 l-3 4 q-8 -6 -10 -18 l5 -2 q3 -1 2 -4 l-3 -11 q-1 -4 -5 -3 z" fill="#ffffff"/>
      </svg>
      <span class="phone-bubble__number">0491 857 604</span>
    </div>

    <p class="bookings">Bookings Essential!</p>
    <p class="website">www.tarovacalm.com.au</p>

    <div class="direction-ribbon">
      <svg width="660" height="80" viewBox="0 0 660 80" aria-hidden="true">
        <path d="M0 8 H590 L632 40 L590 72 H0 Z" fill="#d81f6f" style="filter:drop-shadow(2px 3px 3px rgba(60,20,20,.35))"/>
        <path d="M0 8 H590 L608 22 H0 Z" fill="#e85a98"/>
        <circle cx="98" cy="40" r="24" fill="#ffffff"/>
        <g fill="none" stroke="#ffffff" stroke-width="5">
          <polyline points="530,22 548,40 530,58"/>
          <polyline points="546,22 564,40 546,58"/>
          <polyline points="562,22 580,40 562,58"/>
          <polyline points="578,22 596,40 578,58"/>
        </g>
      </svg>
      <span class="direction-ribbon__name">Tarova Calm</span>
    </div>
  </main>
</body>
</html>
```